Wordpress Design Project SEO/SEM Website

Need an updated more professional look for an SEO/SEM existing site.
see: www.brightpathleads.example

I have an existing logo (in eps format), but am flexible on color and would consider updating the logo if the current colors or design limits your creativity.

Target Market(s)

My customers tend to be marketing managers for mid-size companies with 50+ employees.

Industry/Entity Type

Marketing

Requirements
Must have
• Design should support WordPress 3.0 menus, and widgets.
Nice to have
• Should you want/need it, the font used in the logo is 'ARTLOOKIN'
Should not have
• flash

```html
<!DOCTYPE html>
<html lang="en">
<head>
<meta charset="utf-8">
<title>BrightPath Leads – Internet Marketing</title>
<link href="https://fonts.googleapis.com/css2?family=Cinzel:wght@700&family=Noto+Sans:wght@400;700&display=swap" rel="stylesheet">
<style>
  :root {
    --bg: #62a6d5;
    --bg-deep: #3f8dc0;
    --ink-dark: #1c5a86;
    --ink-black: #0d1f2d;
    --white: #ffffff;
    --soft-white: #d9ecf8;
    --panel: #dbe9f3;
    --panel-text: #1d2c38;
    --green: #5c8c2a;
    --button: #7cb83a;
    --dash: rgba(255,255,255,0.75);
  }
  * { box-sizing: border-box; margin: 0; padding: 0; }
  html, body { width: 1167px; height: 1200px; overflow: hidden; }
  body {
    position: relative;
    background: var(--bg);
    font-family: "Noto Sans", Verdana, sans-serif;
    color: var(--white);
  }
  .abs { position: absolute; }

  .brand-box {
    left: 37px; top: 0; width: 202px; height: 146px;
    background: linear-gradient(#ffffff, #e9eef1);
    border-radius: 0 0 10px 10px;
    box-shadow: 0 2px 4px rgba(0,0,0,0.2);
    display: flex; align-items: center; justify-content: center; gap: 8px;
  }
  .brand-box .dot { width: 16px; height: 16px; border-radius: 50%; background: #1a7a99; }
  .brand-box .name { color: #1a7a99; font-weight: 700; font-size: 19px; }

  .search { left: 801px; top: 28px; display: flex; align-items: center; gap: 10px; font-size: 18px; }
  .search-field {
    width: 247px; height: 33px; background: var(--white); border-radius: 9px;
    position: relative;
  }
  .search-field svg { position: absolute; right: 10px; top: 7px; }

  .nav { top: 125px; left: 0; width: 1167px; height: 22px; font-size: 15px; font-weight: 700; }
  .nav span { position: absolute; letter-spacing: 0.3px; }

  .rule { left: 0; width: 1167px; border-top: 1px dashed var(--dash); }

  .hero-paper {
    left: 44px; top: 203px; width: 450px; height: 300px;
    background: #f3ecd2; transform: rotate(2.2deg);
    box-shadow: 0 2px 5px rgba(0,0,0,0.25);
  }
  .hero-photo {
    left: 8px; top: 217px; width: 477px; height: 314px;
    background: linear-gradient(160deg, #4a93d6 0%, #8cbfe2 55%, #8fbf5a 100%);
  }
  .hero-title { left: 548px; top: 284px; font-family: "Cinzel", Georgia, serif; font-size: 44px; color: var(--ink-dark); }
  .hero-sub { left: 548px; top: 334px; font-size: 23px; letter-spacing: 0.5px; }
  .hero-text { left: 548px; top: 380px; width: 570px; font-size: 13px; line-height: 20px; color: var(--soft-white); }

  .main { left: 28px; top: 599px; width: 545px; }
  .main h1 { font-size: 20px; font-weight: 400; color: var(--ink-black); margin-bottom: 10px; }
  .main p { font-size: 14.5px; line-height: 23.5px; margin-bottom: 3px; }
  .main h2 { font-size: 14.5px; font-weight: 400; color: var(--ink-black); margin-top: 2px; }
  .main .wide { width: 817px; }

  .diagram {
    left: 606px; top: 639px; width: 245px; height: 200px; border-radius: 12px;
    background: linear-gradient(135deg, #2d8fc4 0%, #8aa33e 55%, #b57a32 100%);
    opacity: 0.9;
  }
  .more-btn {
    left: 664px; top: 939px; width: 79px; height: 26px; border-radius: 13px;
    background: var(--button); font-size: 14px; text-align: center; line-height: 26px;
  }

  .client-heading { left: 26px; top: 992px; font-size: 21px; }
  .client-arrow { top: 1050px; font-size: 30px; font-weight: 700; line-height: 30px; }
  .client-card {
    top: 1035px; width: 159px; height: 67px; background: var(--white);
    border: 1px solid #2c6ea0;
    display: flex; align-items: center; justify-content: center;
    color: #2b4b6a; font-weight: 700; font-size: 13px; text-align: center;
  }

  .contact-box {
    left: 870px; top: 585px; width: 285px; height: 84px; border-radius: 8px;
    background: var(--bg-deep); padding: 14px 0 0 18px;
  }
  .contact-box .big { font-size: 25px; line-height: 30px; }
  .contact-box .small { font-size: 19px; color: #8fd0f5; }
  .contact-box svg { position: absolute; right: 20px; top: 10px; }

  .sidebar {
    left: 871px; top: 679px; width: 284px; height: 423px; border-radius: 8px;
    background: var(--panel); padding: 8px 12px 8px 20px; color: var(--panel-text);
  }
  .sidebar h3 { font-size: 15px; font-weight: 400; color: var(--green); margin-bottom: 3px; line-height: 20px; }
  .sidebar ul { list-style: none; font-size: 12.8px; line-height: 22px; margin-bottom: 11px; }
  .badge { width: 140px; height: 31px; background: linear-gradient(#f4f4f4, #9aa0a6); margin: 4px 0 13px; border: 1px solid #7a8086; }

  .copyright { left: 26px; top: 1155px; font-size: 13px; }
  .social { right: 12px; top: 1155px; display: flex; align-items: center; gap: 8px; font-size: 12px; }
  .social .pill { display: flex; align-items: center; gap: 3px; }
  .social .sq { width: 12px; height: 12px; background: #2c5d9c; border-radius: 2px; }
</style>
</head>
<body>
  <header>
    <div class="abs brand-box"><span class="dot"></span><span class="name">BrightPath Leads</span></div>
    <div class="abs search">
      <span>Search :</span>
      <div class="search-field">
        <svg width="22" height="20" viewBox="0 0 22 20"><circle cx="8" cy="8" r="6" fill="none" stroke="#2c4d6b" stroke-width="2.5"/><line x1="12" y1="12" x2="20" y2="18" stroke="#2c4d6b" stroke-width="3" stroke-linecap="round"/></svg>
      </div>
    </div>
    <nav class="abs nav">
      <span style="left:369px">HOME</span>
      <span style="left:459px">SERVICES</span>
      <span style="left:583px">SEO</span>
      <span style="left:658px">SEM</span>
      <span style="left:734px">ABOUT US</span>
      <span style="left:861px">OUR CLIENTS</span>
      <span style="left:1014px">CONTACT US</span>
    </nav>
  </header>
  <div class="abs rule" style="top:171px"></div>

  <section>
    <div class="abs hero-paper"></div>
    <div class="abs hero-photo" role="img" aria-label="Photo of a hand holding puzzle pieces against the sky"></div>
    <div class="abs hero-title">BrightPath Leads</div>
    <div class="abs hero-sub">Internet Marketing, Riverton Valley 40210</div>
    <p class="abs hero-text">BrightPath Leads provides Search Engine Optimization (SEO) and Search Engine Marketing (SEM) services for the Riverton Valley area. Our focus is optimizing and marketing websites to maximize results.</p>
  </section>
  <div class="abs rule" style="top:572px"></div>

  <main class="abs main">
    <h1>Internet Marketing</h1>
    <p>BrightPath Leads provides Search Engine Optimization (SEO) and Search Engine Marketing (SEM) services for the Riverton Valley area. Our focus is optimizing and marketing websites to maximize results.</p>
    <p>Searchly’s algorithm employs over 200 variables in determining the ranking of sites. At the core of the algorithm are three elements: Quality Content, Site Architecture, and Incoming Links.</p>
    <p>Searchly’s algorithm employs over 200 variables in determining the ranking of sites. At the core of the algorithm are three elements: Quality Content, Site Architecture, and Incoming Links.</p>
    <h2>Quality Content</h2>
    <p class="wide">Your site’s content must convey its purpose in a clear fashion and, within seconds, convince your visitors that they have found something worth further exploration. In order for the search engine to target your content, however, the copy must contain key phrases that can be married to the searchers’ requests.</p>
  </main>

  <div class="abs diagram" role="img" aria-label="Illustration of three overlapping spheres labelled Content, Incoming Links and Site Architecture"></div>
  <div class="abs more-btn">more</div>
  <div class="abs rule" style="top:980px; left:12px; width:845px"></div>

  <section>
    <div class="abs client-heading">Client list</div>
    <div class="abs client-arrow" style="left:28px">‹</div>
    <div class="abs client-card" style="left:55px">Northfield Pipe Co.</div>
    <div class="abs client-card" style="left:222px">Harbor Family Center</div>
    <div class="abs client-card" style="left:389px">Willowmere School</div>
    <div class="abs client-card" style="left:557px">Lakeside University</div>
    <div class="abs client-arrow" style="left:728px">›</div>
  </section>

  <aside>
    <div class="abs contact-box">
      <div class="big">Contact us</div>
      <div class="small">Today</div>
      <svg width="88" height="70" viewBox="0 0 88 70"><rect x="4" y="16" width="80" height="50" rx="3" fill="#f2c23a"/><path d="M4 16 L44 46 L84 16" fill="#fbe08a" stroke="#d89d1a" stroke-width="2"/></svg>
    </div>
    <div class="abs sidebar">
      <h3>Posts by Category</h3>
      <ul><li>SEM Riverton (44)</li><li>SEO Riverton (46)</li><li>Web Analytics (10)</li></ul>
      <h3>Member</h3>
      <div class="badge"></div>
      <h3>Recent Blog Posts</h3>
      <ul>
        <li>What is duplicate content?</li>
        <li>How to Create an Effective Website</li>
        <li>Dealing with bad reviews in Searchly<br>Places</li>
        <li>Cartoon Exposes the Dark Side of SEO</li>
        <li>Don’t use PDFs as Web Pages</li>
      </ul>
      <h3>Meta</h3>
      <ul><li>Log in</li></ul>
    </div>
  </aside>

  <div class="abs rule" style="top:1134px"></div>
  <footer>
    <div class="abs copyright">© BrightPath-Leads 2010 - All Rights Reserved</div>
    <div class="abs social">
      <span>x25</span>
      <span class="pill"><span class="sq"></span>Friendly</span>
      <span class="pill"><span class="sq"></span>Chirpnet</span>
    </div>
  </footer>
</body>
</html>
```